Company Values Graphic

We are looking for a design of our company values that can be used in a variety of places including our website, mousepads, office posters, business cards, etc.

Notes:
- We'd rather have icons/art than photographs on the poster.... so more like an infographic
- The core value group headings are not required, but can be included if you think grouping the values works for your design
- We have a logo for our software product but that logo is not required
- We don't need/want clever images to accompany each value, but some images are fine
- BrisKel logo attached
- BrisKel colors are attached
- BrisKel logo is Nunito Sans ExtraBold 800
- BrisKel website uses Roboto

Our Values - Who we will work with (and who we will not)
The right set of values are essential to building and maintaining a culture that we all wake up eager to be a part of each day. They are foundational to all hiring and firing decisions. They attract the right people and repel the wrong ones.

BE HELPFUL
Make every person and place better because you are there.
Deliver wow with every interaction.

BE HUMBLE
Listen with every muscle.
Passionately help others first.
Seek first to understand.

BE HONEST
Earn trust every day.
Be open and direct.
Treat everyone with fairness and respect.

BE HUMAN
Celebrate passion and action.
Create an environment where people are authentic.
Hire great people and expect a lot from them

BE COURAGEOUS
Dare mighty things.
Make and honor commitments.
All great things start with a small act of courage applied at the right moment.

```html
<!DOCTYPE html>
<html lang="en">
<head>
<meta charset="utf-8">
<title>Our Values</title>
<link rel="stylesheet" href="https://fonts.googleapis.com/css2?family=Montserrat:wght@800;900&family=Nunito:wght@300;400;800&display=swap">
<style>
  :root {
    --brand-orange: #f15a24;
    --flame-yellow: #f7a01d;
    --flame-red: #ed2128;
    --ink: #231f20;
    --paper: #ffffff;
  }
  * { margin: 0; padding: 0; box-sizing: border-box; }
  html, body { width: 1200px; height: 1000px; overflow: hidden; background: var(--paper); }
  .canvas { position: relative; width: 1200px; height: 1000px; color: var(--ink); font-family: "Nunito", Arial, sans-serif; }

  .page-title {
    position: absolute; top: 110px; left: 0; width: 1200px; text-align: center;
    font-family: "Montserrat", Arial, sans-serif; font-weight: 900; font-size: 21px;
    letter-spacing: 31px; padding-left: 31px; line-height: 26px;
  }
  .rule { position: absolute; top: 183px; height: 31px; background: var(--brand-orange); }
  .rule--left { left: 0; width: 378px; }
  .rule--right { left: 821px; width: 379px; }
  .subtitle {
    position: absolute; top: 181px; left: 378px; width: 443px; text-align: center;
    font-family: "Montserrat", Arial, sans-serif; font-weight: 800; font-size: 19px; line-height: 18px;
  }

  .hero-art {
    position: absolute; left: 534px; top: 277px; width: 132px; height: 226px; border-radius: 66px 66px 40px 40px;
    background: linear-gradient(160deg, var(--flame-yellow) 0%, var(--brand-orange) 45%, var(--flame-red) 75%, #ffffff 100%);
    opacity: 0.9;
  }

  .intro { position: absolute; font-size: 18.5px; font-weight: 400; line-height: 23px; white-space: nowrap; }
  .intro--l1a { top: 463px; right: 686px; }
  .intro--l1b { top: 463px; left: 678px; }
  .intro--l2a { top: 486px; right: 688px; }
  .intro--l2b { top: 486px; left: 655px; }
  .intro--l3 { top: 509px; left: 0; width: 1200px; text-align: center; }
  .intro--l4 { top: 533px; left: 0; width: 1200px; text-align: center; }

  .value-card {
    position: absolute; width: 183px; height: 157px; background: var(--brand-orange);
    border-radius: 12px; padding: 0 3px 3px; display: flex; flex-direction: column; z-index: 2;
  }
  .value-card__title {
    height: 40px; display: flex; align-items: center; justify-content: center;
    color: var(--paper); font-weight: 800; font-size: 17.5px; letter-spacing: 0.2px;
  }
  .value-card__body {
    flex: 1; background: var(--paper); border-radius: 9px; padding: 16px 6px 0;
    text-align: center; font-size: 11.6px; font-weight: 400; line-height: 14.4px;
  }
  .value-card--helpful { left: 318px; top: 580px; }
  .value-card--humble { left: 510px; top: 580px; }
  .value-card--human { left: 702px; top: 580px; }
  .value-card--honest { left: 414px; top: 747px; }
  .value-card--courageous { left: 606px; top: 747px; }

  .link { position: absolute; background: var(--brand-orange); z-index: 1; }
  .link--row1a { left: 498px; top: 655px; width: 14px; height: 8px; }
  .link--row1b { left: 690px; top: 655px; width: 14px; height: 8px; }
  .link--row2 { left: 594px; top: 831px; width: 14px; height: 8px; }
  .link--elbow-left {
    left: 386px; top: 735px; width: 32px; height: 104px;
    background: transparent; border: 9px solid var(--brand-orange); border-top: 0; border-right: 0;
    border-radius: 0 0 0 12px;
  }
  .link--elbow-right {
    left: 785px; top: 735px; width: 30px; height: 104px;
    background: transparent; border: 9px solid var(--brand-orange); border-top: 0; border-left: 0;
    border-radius: 0 0 12px 0;
  }
</style>
</head>
<body>
<main class="canvas">
  <h1 class="page-title">OUR VALUE</h1>

  <div class="rule rule--left"></div>
  <div class="rule rule--right"></div>
  <h2 class="subtitle">WHO WE WILL WORK WITH<br>(AND WHO WE WILL NOT)</h2>

  <div class="hero-art" role="img" aria-label="Illustration of a figure holding up a flame in red, orange and yellow"></div>

  <p class="intro intro--l1a">The right set of values are</p>
  <p class="intro intro--l1b">essential to building and</p>
  <p class="intro intro--l2a">maintaining a culture that</p>
  <p class="intro intro--l2b">we all wake up eager to be a</p>
  <p class="intro intro--l3">part of each day. They are foundational to all hiring and firing decisions.</p>
  <p class="intro intro--l4">They attract the right people and repel the wrong ones.</p>

  <div class="link link--row1a"></div>
  <div class="link link--row1b"></div>
  <div class="link link--row2"></div>
  <div class="link link--elbow-left"></div>
  <div class="link link--elbow-right"></div>

  <section class="value-card value-card--helpful">
    <h3 class="value-card__title">BE HELPFUL</h3>
    <p class="value-card__body">Make every person and place better because you are there.<br>Deliver wow with every interaction.</p>
  </section>
  <section class="value-card value-card--humble">
    <h3 class="value-card__title">BE HUMBLE</h3>
    <p class="value-card__body">Listen with every muscle.<br>Passionately help others first.<br>Seek first to understand.</p>
  </section>
  <section class="value-card value-card--human">
    <h3 class="value-card__title">BE HUMAN</h3>
    <p class="value-card__body">Celebrate passion and action.<br>Create an environment where people are authentic.<br>Hire great people and expect a lot from them</p>
  </section>
  <section class="value-card value-card--honest">
    <h3 class="value-card__title">BE HONEST</h3>
    <p class="value-card__body">Earn trust every day.<br>Be open and direct.<br>Treat everyone with fairness and respect.</p>
  </section>
  <section class="value-card value-card--courageous">
    <h3 class="value-card__title">BE COURAGEOUS</h3>
    <p class="value-card__body">Dare mighty things.<br>Make and honor commitments.<br>All great things start with a small act of courage applied at the right moment.</p>
  </section>
</main>
</body>
</html>
```